Business Card Design

We need a business card design for an existing business. Our main trading brand is www.brightmeadowsaver.co.uk

We attach various logo files - please use the version that will produce the sharpest image on the business card.

We are flexible about shape of card etc. Please think outside the box as to what goes on front and what goes on back of the card

We want to be able to amend the card (once the design has been agreed ) to add additional staff details, but the text to go on it will be generic

Details to go on card ( for the first generic one) are fairly minimal as we don't like cluttered business cards:-

Tom Harker
Managing Director

Mobile: 07812 548 207
Email: t.harker@brightmeadowsaver.co.uk

```html
<!DOCTYPE html>
<html lang="en">
<head>
<meta charset="utf-8">
<title>Bright Meadow Saver – Business Card</title>
<link rel="stylesheet" href="https://fonts.googleapis.com/css2?family=Open+Sans:wght@400;600&display=swap">
<style>
  :root {
    --backdrop: #e4e6e8;
    --card: #ffffff;
    --brand-blue: #2a9bd6;
    --navy: #1f3f5f;
    --text-grey: #4d4f52;
    --card-shadow: 0 10px 28px rgba(0, 0, 0, 0.18);
  }
  * { box-sizing: border-box; margin: 0; padding: 0; }
  html, body {
    width: 1200px;
    height: 900px;
    overflow: hidden;
  }
  body {
    background: var(--backdrop);
    font-family: "Open Sans", Arial, sans-serif;
    display: flex;
    flex-direction: column;
    align-items: center;
    justify-content: center;
    gap: 44px;
  }
  .card {
    width: 660px;
    height: 377px;
    background: var(--card);
    box-shadow: var(--card-shadow);
    position: relative;
  }
  .brand {
    display: flex;
    align-items: center;
    gap: 10px;
  }
  .brand-name {
    font-weight: 400;
    color: var(--brand-blue);
    letter-spacing: 0.2px;
  }
  .brand-dot {
    width: 14px;
    height: 14px;
    border-radius: 50%;
    background: var(--brand-blue);
  }

  /* Back of card */
  .card-back .brand {
    position: absolute;
    right: 44px;
    bottom: 58px;
  }
  .card-back .brand-name { font-size: 22px; }

  /* Front of card */
  .card-front {
    display: flex;
    align-items: center;
    padding-left: 34px;
  }
  .card-front .brand-name { font-size: 21px; }
  .divider {
    width: 2px;
    height: 92px;
    background: var(--navy);
    margin: 0 24px 0 22px;
  }
  .contact-name {
    font-size: 19px;
    font-weight: 600;
    color: var(--brand-blue);
    line-height: 1.15;
  }
  .contact-role {
    font-size: 15px;
    color: var(--text-grey);
    margin-bottom: 6px;
  }
  .contact-line {
    display: flex;
    align-items: center;
    gap: 8px;
    font-size: 15px;
    color: var(--text-grey);
    line-height: 1.55;
  }
  .contact-line svg { width: 14px; height: 14px; fill: var(--navy); flex: none; }
</style>
</head>
<body>
  <section class="card card-back" aria-label="Back of business card">
    <div class="brand">
      <span class="brand-name">brightmeadowsaver.co.uk</span>
      <span class="brand-dot"></span>
    </div>
  </section>

  <section class="card card-front" aria-label="Front of business card">
    <div class="brand">
      <span class="brand-name">brightmeadowsaver.co.uk</span>
      <span class="brand-dot"></span>
    </div>
    <div class="divider"></div>
    <div class="contact">
      <p class="contact-name">Tom Harker</p>
      <p class="contact-role">Managing Director</p>
      <p class="contact-line">
        <svg viewBox="0 0 24 24" aria-hidden="true"><path d="M6.6 10.8a15.1 15.1 0 0 0 6.6 6.6l2.2-2.2c.3-.3.7-.4 1-.2 1.1.4 2.3.6 3.6.6.6 0 1 .4 1 1V20c0 .6-.4 1-1 1A17 17 0 0 1 3 4c0-.6.4-1 1-1h3.5c.6 0 1 .4 1 1 0 1.3.2 2.5.6 3.6.1.3 0 .7-.2 1l-2.3 2.2z"/></svg>
        07812 548 207
      </p>
      <p class="contact-line">
        <svg viewBox="0 0 24 24" aria-hidden="true"><path d="M2 5h20v14H2z M3.5 6.5 12 13l8.5-6.5" fill="none" stroke="#1f3f5f" stroke-width="0"/><path d="M2 5h20v14H2V5zm2 1.6V17h16V6.6l-8 6.1-8-6.1zM5.3 6.5 12 11.6l6.7-5.1H5.3z"/></svg>
        t.harker@brightmeadowsaver.co.uk
      </p>
    </div>
  </section>
</body>
</html>
```